Website Design Brief for KTR LEGAL PTY LTD

Company Name: KTR LEGAL PTY LTD

Industry: Legal Services

Target Audience:

Corporate clients
Business owners
Individuals seeking legal advice in Commercial Law, Mergers and Acquisitions, Will Law, Property Law, and Conveyancing
Objective:

To create a professional, user-friendly website that establishes trust and authority in the legal field.
Provide easy access to information about the firm’s services, team, and areas of expertise.
Include client testimonials, contact information, and a blog or resource section for legal insights.
Key Features and Pages:

Homepage:

Clean, modern design with a professional feel.
Introduction to KTR LEGAL with a brief overview of services.
High-quality images or illustrations related to law and professionalism.
Prominent call-to-action (CTA) like "Get in Touch" or "Book a Consultation."
About Us:

Information about the firm's mission, values, and team.
Highlight the expertise and experience of key members.
Include a brief company history, if relevant.
Services:

Detailed descriptions of services, categorized by legal areas (e.g., Commercial Law, Mergers & Acquisitions, Property Law, etc.).
Call-to-action buttons to encourage potential clients to reach out for consultations.
Team:

Profiles of key team members, including their qualifications, expertise, and professional photos.
Include links to their professional networks (LinkPlaza).
Testimonials:

Section showcasing positive client testimonials or case studies.
This can help build trust and credibility with potential clients.
Blog or Resources:

A blog or resources section providing legal tips, industry news, and insights.
Content should demonstrate the firm’s knowledge and thought leadership.
Contact Us:

Easy-to-use contact form.
Include phone number, email, physical office address, and possibly a map.
Option for booking consultations or initial meetings directly online.
Client Portal (optional):

Secure login for clients to access their case information, documents, and updates (this could be an advanced feature to consider after launch).
Design Aesthetic:

Clean, modern, and professional.
Elegant use of fonts and a color palette that reflects trust, authority, and sophistication (dark blues, whites, grays).
User-friendly navigation to ensure clients can easily find the information they need.
Technical Considerations:

The website should be mobile-responsive and look great on all devices (desktop, tablet, mobile).
Ensure fast load times and optimized images.
Implement SEO best practices to improve search engine rankings.
Easy-to-update CMS (WordPress or similar) to allow easy future updates.
Competitor/Inspirational Websites:

[Provide examples of legal firms' websites you like, or any designs that reflect the feel you want for your firm.]
Additional Information:

Please ensure all content is aligned with the firm's professional tone and approach.
The website should be designed to be scalable for future growth (adding more services, resources, etc.).

Target Market(s)

Business owners Individuals seeking legal advice in Commercial Law, Mergers and Acquisitions, Will Law, Property Law, and Conveyancing

Industry/Entity Type

Legal

Number of Pages Required

3 page

Requirements
Must have
• Home Page, About Us, Contact Us, Services

```html
<!DOCTYPE html>
<html lang="en">
<head>
<meta charset="utf-8">
<title>KTR LEGAL PTY LTD</title>
<link href="https://fonts.googleapis.com/css2?family=Mulish:wght@400;600;700;800&family=Inter:wght@400;500;600&display=swap" rel="stylesheet">
<style>
:root{
  --navy:#05336b;
  --navy-deep:#042b5b;
  --blue:#0b56b1;
  --pale:#e8eef7;
  --cream:#f8f7f2;
  --ink:#1b1b1b;
  --muted:#8a8f98;
  --white:#ffffff;
  --field:#ffffff;
  --form-bg:#f4f6f9;
}
*{box-sizing:border-box;margin:0;padding:0}
html,body{width:1200px;height:4270px;overflow:hidden}
body{font-family:"Inter",sans-serif;color:var(--ink);background:var(--pale);position:relative}
.abs{position:absolute}
.heading{font-family:"Mulish",sans-serif}
.btn{position:absolute;display:flex;align-items:center;justify-content:center;background:var(--blue);color:var(--white);font-family:"Mulish",sans-serif;font-weight:700;font-size:17px}
.photo{position:absolute}

/* nav */
.site-nav{position:absolute;left:0;top:0;width:1200px;height:53px;background:var(--navy);z-index:3}
.brand{position:absolute;font-family:"Mulish",sans-serif;font-weight:600;color:var(--white);letter-spacing:1px}
.site-nav .brand{left:66px;top:12px;font-size:24px}
.nav-links{position:absolute;right:66px;top:18px;display:flex;gap:34px;font-family:"Mulish",sans-serif;font-size:13px;color:var(--white);font-weight:600}
.nav-links .active{font-weight:800}

/* hero */
.hero{left:0;top:53px;width:1200px;height:514px;background:linear-gradient(180deg,#2a221d 0%,#4a3c30 45%,#2b241f 100%)}
.hero-title{left:0;top:102px;width:1200px;text-align:center;color:var(--white);font-family:"Mulish",sans-serif;font-weight:600;font-size:34px;line-height:42px}
.hero-sub{left:0;top:182px;width:1200px;text-align:center;color:var(--white);font-family:"Mulish",sans-serif;font-weight:700;font-size:13px;line-height:16px}

/* about */
.about{left:60px;top:482px;width:1080px;height:409px;background:var(--navy);color:var(--white);text-align:center}
.about h2{position:absolute;top:78px;width:100%;font-family:"Mulish",sans-serif;font-weight:600;font-size:33px}
.about p{position:absolute;left:64px;top:146px;width:952px;font-size:16.5px;line-height:26.7px}

/* services */
.service{position:absolute;top:1036px;width:216px;text-align:center}
.service svg{display:block;margin:0 auto}
.service h3{font-family:"Mulish",sans-serif;font-weight:700;font-size:16px;margin-top:14px}
.service p{margin:8px auto 0;width:200px;text-align:justify;font-size:13.5px;line-height:16px}

/* cta band */
.cta-band{left:0;top:1417px;width:1200px;height:217px;background:var(--navy)}
.cta-band h2{position:absolute;top:54px;width:100%;text-align:center;color:var(--white);font-family:"Mulish",sans-serif;font-weight:600;font-size:27px}

/* sections */
.section-title{position:absolute;left:0;width:1200px;text-align:center;color:var(--navy);font-family:"Mulish",sans-serif;font-weight:700;font-size:33px}

/* attorneys */
.attorney{position:absolute;top:1776px;width:346px;text-align:center}
.attorney .photo{position:relative;width:346px;height:345px;background:linear-gradient(180deg,#ffffff 0%,#f1f1f1 50%,#2d2f33 100%)}
.attorney h3{margin-top:12px;font-family:"Mulish",sans-serif;font-weight:700;font-size:20px}
.attorney .role{margin-top:8px;font-family:"Mulish",sans-serif;font-weight:700;font-size:13px;color:var(--blue)}
.socials{display:flex;justify-content:center;gap:12px;margin-top:14px}
.socials span{width:18px;height:18px;border-radius:50%;background:var(--white);border:1px solid #d8dde5}

/* testimonial */
.quote-rule{left:121px;top:2424px;width:2px;height:161px;background:var(--blue)}
.quote-mark{left:112px;top:2456px;color:var(--blue);font-family:"Mulish",sans-serif;font-size:24px;background:var(--pale);padding:2px 0}
.quote-text{left:151px;top:2460px;width:420px;font-size:17px;line-height:22px}
.quote-name{left:151px;top:2542px;font-family:"Mulish",sans-serif;font-weight:600;font-size:21px}
.quote-role{left:151px;top:2577px;font-family:"Mulish",sans-serif;font-weight:700;font-size:13px;color:var(--blue)}

/* consultation */
.consult{left:0;top:2714px;width:1200px;height:756px;background:var(--navy);color:var(--white)}
.consult .brand{left:151px;top:214px;font-size:40px}
.consult h2{position:absolute;left:151px;top:288px;font-family:"Mulish",sans-serif;font-weight:700;font-size:34px;line-height:42px}
.consult .lead{position:absolute;left:151px;top:404px;width:340px;font-size:13px;line-height:22px}
.form{position:absolute;left:610px;top:99px;width:437px;height:556px;background:var(--form-bg);color:var(--ink);padding:33px}
.field{position:absolute}
.field label{display:block;font-family:"Mulish",sans-serif;font-weight:700;font-size:13px;margin-bottom:7px}
.field .input{height:38px;background:var(--field);color:#b2b6bc;font-size:12.5px;padding:11px 14px;position:relative}
.field .area{height:160px}

/* blog */
.blog{left:0;top:3470px;width:1200px;height:512px;background:var(--cream)}
.blog .sub{position:absolute;top:94px;width:1200px;text-align:center;font-size:16.5px}
.post{position:absolute;top:139px;width:346px}
.post .photo{position:relative;width:346px;height:232px}
.post .date{margin-top:10px;font-size:13px;color:#444}
.post h3{margin-top:10px;font-family:"Mulish",sans-serif;font-weight:700;font-size:16.5px;color:var(--blue)}
.post .more{margin-top:14px;font-size:9.5px;font-weight:600;display:flex;align-items:center;gap:6px;letter-spacing:.3px}

/* footer */
.footer{left:0;top:3982px;width:1200px;height:288px;background:var(--navy);color:var(--white)}
.footer .brand{left:60px;top:52px;font-size:24px}
.footer .blurb{position:absolute;left:60px;top:108px;width:245px;font-size:12.5px;line-height:22px}
.footer .socials{position:absolute;left:60px;top:185px;margin:0;gap:10px}
.footer .socials span{width:16px;height:16px;border:none}
.fcol{position:absolute;top:52px;font-size:13px;line-height:30px}
.fcol h4{font-family:"Mulish",sans-serif;font-weight:600;font-size:17px;margin-bottom:10px;line-height:22px}
.copyright{position:absolute;top:254px;width:1200px;text-align:center;font-size:12.5px;color:#c9d3e2}
</style>
</head>
<body>

<header class="site-nav">
  <div class="brand">KTR LEGAL</div>
  <nav class="nav-links"><span class="active">Home</span><span>About us</span><span>Services</span><span>Contact us</span></nav>
</header>

<section class="abs hero" role="img" aria-label="Courthouse columns and steps at dusk"></section>
<h1 class="abs hero-title">TRUSTED LEGAL EXPERTISE SOLUTIONS<br>FOR BUSINESSES &amp; INDIVIDUALS</h1>
<p class="abs hero-sub">Specializing in Commercial Law, Mergers &amp;<br>Acquisitions, Wills, Property Law &amp; Conveyancing</p>
<a class="btn" style="left:492px;top:351px;width:215px;height:42px">Book a Consultation</a>

<section class="abs about">
  <h2>About Us</h2>
  <p>At KTR LEGAL PTY LTD, we are committed to providing expert legal solutions tailored to the needs of businesses, corporate clients, and individuals. With a strong focus on Commercial Law, Mergers &amp; Acquisitions, Wills, Property Law, and Conveyancing, our experienced team delivers strategic legal advice and practical solutions to protect your interests and help you navigate complex legal matters.<br>We pride ourselves on our client-focused approach, ensuring clear communication, personalized service, and cost-effective legal strategies. Whether you are a business owner managing corporate transactions or an individual seeking legal guidance, KTR LEGAL PTY LTD is your trusted partner in legal excellence.</p>
</section>

<div class="service" style="left:151px">
  <svg width="32" height="32" viewBox="0 0 32 32"><rect x="7" y="4" width="20" height="24" rx="2" fill="var(--blue)"/><rect x="11" y="10" width="12" height="2" fill="#fff"/><rect x="11" y="15" width="12" height="2" fill="#fff"/><rect x="11" y="20" width="8" height="2" fill="#fff"/></svg>
  <h3>Commercial Law</h3>
  <p>Lorem ipsum dolor sit amet consectetur. Massa sed dapibus adipiscing felis at. Integer at dictum ullamcorper magna nam eget.</p>
</div>
<div class="service" style="left:492px">
  <svg width="32" height="32" viewBox="0 0 32 32"><path d="M16 4 L28 14 V28 H4 V14 Z" fill="var(--blue)"/><circle cx="16" cy="19" r="4" fill="#fff"/></svg>
  <h3>Property law</h3>
  <p>Lorem ipsum dolor sit amet consectetur. Massa sed dapibus adipiscing felis at. Integer at dictum ullamcorper magna nam eget.</p>
</div>
<div class="service" style="left:833px">
  <svg width="32" height="32" viewBox="0 0 32 32"><path d="M24 3 L29 8 L12 25 L6 27 L8 21 Z" fill="var(--blue)"/><rect x="3" y="28" width="14" height="2" fill="var(--blue)"/></svg>
  <h3>Mergers &amp; Acquisitions</h3>
  <p>Lorem ipsum dolor sit amet consectetur. Massa sed dapibus adipiscing felis at. Integer at dictum ullamcorper magna nam eget.</p>
</div>
<a class="btn" style="left:151px;top:1231px;width:215px;height:42px">Learn More</a>
<a class="btn" style="left:492px;top:1231px;width:215px;height:42px">Learn More</a>
<a class="btn" style="left:833px;top:1231px;width:216px;height:42px">Learn More</a>

<section class="abs cta-band"><h2>Have Legal Questions? Ask Our Experts!</h2></section>
<a class="btn" style="left:519px;top:1538px;width:162px;height:41px">Ask an expert</a>

<h2 class="section-title" style="top:1673px">Our Attorneys</h2>
<div class="attorney" style="left:60px">
  <div class="photo" role="img" aria-label="Portrait of a bearded attorney in a dark suit"></div>
  <h3>Daniel Marsh</h3><div class="role">Finance Lawyer</div>
  <div class="socials"><span></span><span></span><span></span><span></span></div>
</div>
<div class="attorney" style="left:427px">
  <div class="photo" role="img" aria-label="Portrait of an attorney in a black blazer"></div>
  <h3>Clara Hensley</h3><div class="role">Criminal Defence Lawyer</div>
  <div class="socials"><span></span><span></span><span></span><span></span></div>
</div>
<div class="attorney" style="left:794px">
  <div class="photo" role="img" aria-label="Portrait of a smiling attorney in a dark suit"></div>
  <h3>Owen Pritchard</h3><div class="role">Tax Lawyer</div>
  <div class="socials"><span></span><span></span><span></span><span></span></div>
</div>

<h2 class="section-title" style="top:2344px">What Our Client Says</h2>
<p class="abs" style="left:0;top:2395px;width:1200px;text-align:center;font-size:13px">Our&nbsp; Testimonials</p>
<div class="abs quote-rule"></div>
<div class="abs quote-mark">“</div>
<p class="abs quote-text">Lorem ipsum dolor sit amet consectetur. Massa sed dapibus adipiscing felis at. Integer at dictum ullamcorper magna nam eget.</p>
<div class="abs quote-name">Laurens Voss</div>
<div class="abs quote-role">Founder Norvale LTD</div>
<div class="photo" style="left:794px;top:2424px;width:254px;height:206px;background:linear-gradient(135deg,#c7d2dc 0%,#8c9aa7 55%,#1f2730 100%)" role="img" aria-label="Portrait of a client wearing glasses outdoors"></div>

<section class="abs consult">
  <div class="brand">KTR LEGAL</div>
  <h2>Request A<br>Consultation</h2>
  <p class="lead">Lorem ipsum dolor sit amet consectetur. Massa sed dapibus adipiscing felis at. Integer at dictum ullamcorper magna nam eget.</p>
  <div class="form">
    <div class="field" style="left:33px;top:33px;width:176px"><label>Name</label><div class="input">Your Name</div></div>
    <div class="field" style="left:228px;top:33px;width:176px"><label>Phone</label><div class="input">Your Phone</div></div>
    <div class="field" style="left:33px;top:115px;width:176px"><label>Email</label><div class="input">Your Email</div></div>
    <div class="field" style="left:228px;top:115px;width:176px"><label>Service</label><div class="input">Civil Law
      <svg style="position:absolute;right:14px;top:15px" width="12" height="8" viewBox="0 0 12 8"><path d="M1 1 L6 6 L11 1" stroke="#555" stroke-width="1.5" fill="none"/></svg></div></div>
    <div class="field" style="left:33px;top:197px;width:371px"><label>Subject</label><div class="input">Subject</div></div>
    <div class="field" style="left:33px;top:279px;width:371px"><label>Message</label><div class="input area">Message</div></div>
    <a class="btn" style="left:33px;top:482px;width:371px;height:41px">Book a Consultation</a>
  </div>
</section>

<section class="abs blog">
  <h2 class="section-title" style="top:40px">Our Blog</h2>
  <p class="sub">Lorem ipsum dolor sit amet consectetur. Massa sed dapibus adipiscing felis at.</p>
  <article class="post" style="left:60px">
    <div class="photo" role="img" aria-label="Statue of justice holding scales before a courthouse" style="background:linear-gradient(90deg,#2f4a5c 0%,#5d7380 60%,#c46a3a 100%)"></div>
    <div class="date">March 24,2025</div><h3>Lorem ipsum dolor sit amet consectetur</h3>
    <div class="more">READ MORE <svg width="10" height="8" viewBox="0 0 10 8"><path d="M0 4 H9 M6 1 L9 4 L6 7" stroke="#222" fill="none"/></svg></div>
  </article>
  <article class="post" style="left:427px">
    <div class="photo" role="img" aria-label="Two professionals shaking hands over a desk" style="background:linear-gradient(135deg,#2c2622 0%,#6e5a48 55%,#d9cfc2 100%)"></div>
    <div class="date">March 16,2025</div><h3>Lorem ipsum dolor sit amet consectetur</h3>
    <div class="more">READ MORE <svg width="10" height="8" viewBox="0 0 10 8"><path d="M0 4 H9 M6 1 L9 4 L6 7" stroke="#222" fill="none"/></svg></div>
  </article>
  <article class="post" style="left:794px">
    <div class="photo" role="img" aria-label="Two colleagues reviewing documents outside office towers" style="background:linear-gradient(135deg,#a9b7c2 0%,#6f8a6a 55%,#2d3a2c 100%)"></div>
    <div class="date">March 5,2025</div><h3>Lorem ipsum dolor sit amet consectetur</h3>
    <div class="more">READ MORE <svg width="10" height="8" viewBox="0 0 10 8"><path d="M0 4 H9 M6 1 L9 4 L6 7" stroke="#222" fill="none"/></svg></div>
  </article>
</section>

<footer class="abs footer">
  <div class="brand">KTR LEGAL</div>
  <p class="blurb">Adipiscing nam neque hendrerit nec pellentesque diam a. Varius quisque odio mauris lectus consequat sed.</p>
  <div class="socials"><span></span><span></span><span></span><span></span></div>
  <div class="fcol" style="left:426px"><h4>Links</h4>Home<br>About Us<br>Services<br>Contact Us</div>
  <div class="fcol" style="left:610px;width:220px;line-height:22px"><h4>Find Us</h4>18 Harbour Crest Lane Brookfield<br>QX 40217<div style="margin-top:8px">(555) 014-2290</div><div style="margin-top:8px">hello@ktrlegal.example</div></div>
  <div class="fcol" style="left:885px"><h4>Practice Areas</h4>Commercial Law<br>Mergers &amp; Acquisitions<br>Banking and Finance<br>Property Law</div>
  <div class="copyright">©Copyright KTR Legal 2025</div>
</footer>

</body>
</html>
```